Luxury Inclusive Beauty Brand Needs Labels & Boxes for Product Line

We need updated labels and boxes for our cosmetic and skin care line. Our company is MAVRA & CO. and we focus on providing upscale, natural and organic beauty products inclusive of diverse and deeper skin tones for women of color, especially black women. We have a seven piece skin care collection called DERMAVELLE Baobin Collection and a mineral make-up line consisting of eight products. The design of all products should be the same with just dimensions and title/ingredient list differences. We would like to see designs that use our coral color e85350, work well on black packaging (bottles, lipstick tubes etc.) and include white and other additional pretty colors, metallics or patterns representative of ethnic (AFRICAN), bohemian or tribal influence. The final design should communicate luxury, floral/fauna environmentalism, and afrocentric culture influences.
We have included files of various prints we like and the type of lifestyle our customer aspires to/is attracted to. We have included in the files below some examples of packaging we like but we want something original to capture the attention of our target market, upper income health and ethnic conscious black women age 30 - 55 who love natural and organic products. The names of our products include the list below however if design can be submitted showing design on 1 tall box and 1 short box and 1 lipstick size box that would be great:
DERMAVELLE Baobin Collection Cleansing Oil (dropper)
DERMAVELLE Baobin Collection Balancing Toner (tall spray bottle)
DERMAVELLE Baobin Collection Moisturizing Serum (dropper)
DERMAVELLE Baobin Collection Moisturizing Cream (short box jar)
DERMAVELLE Baobin Lip Scrub (short box - jar)
Luminous Mineral Foundation (short box- jar)
CC Cream
Moisturizing Lip Stick (lipstick box)
OTIRAFLIX Natural Mascara
Zarra Bimble Lip Crayon
Gel Eye Liner
Organic Make-up Remover (tall spray bottle)
Face & Eye Primer
Final dimensions /dies of boxes can be sent to winner of design competition.
Target Market(s)
women of color, age 30-55, income 50 - 150K, natural hair and organic lifestyle, yoga
Industry/Entity Type
Cosmetics
Requirements
Must have
- label and box
- include the color e85350
- include logo
Nice to have
- easy way to differentiate skincare from make-up products

```html
<!DOCTYPE html>
<html lang="en">
<head>
<meta charset="utf-8">
<title>MAVRA &amp; CO. Packaging</title>
<link href="https://fonts.googleapis.com/css2?family=Montserrat:wght@400;500;600&family=Great+Vibes&display=swap" rel="stylesheet">
<style>
  :root {
    --bg: #d8d8d8;
    --white: #f4f4f4;
    --black: #050505;
    --gold: #d9962f;
    --gold-light: #f0ab3c;
    --gold-dark: #c9781d;
    --coral: #e85350;
    --teal: #1fa68a;
  }
  html, body { margin: 0; padding: 0; overflow: hidden; }
  body { width: 1200px; height: 1029px; background: var(--bg); position: relative; font-family: "Montserrat", sans-serif; }
  .box { position: absolute; display: flex; box-shadow: 14px 12px 22px rgba(0,0,0,0.12); }
  .box-side { height: 100%; background: linear-gradient(135deg, var(--coral) 0%, #e9b7a8 35%, var(--teal) 70%, #e8e0d8 100%); }
  .box-side.dark { background: linear-gradient(135deg, #1a1a1a 0%, var(--coral) 40%, #141414 60%, var(--teal) 100%); }
  .box-front { position: relative; height: 100%; background: var(--white); color: var(--gold); }
  .box-front.dark { background: var(--black); }
  .brand-band { position: absolute; left: 0; right: 0; display: flex; align-items: center; justify-content: center; gap: 8px;
    background: linear-gradient(90deg, var(--gold-dark), var(--gold-light) 45%, var(--gold) 100%); color: #fff; font-weight: 500; letter-spacing: 0.02em; }
  .brand-dot { border: 1.5px solid #fff; border-radius: 50%; }
  .product-line { position: absolute; writing-mode: vertical-rl; transform: rotate(180deg); font-weight: 500; letter-spacing: 0.01em; line-height: 1; color: var(--gold); }
  .collection { position: absolute; font-family: "Great Vibes", cursive; line-height: 0.9; color: var(--gold); }
  .product-name { position: absolute; font-weight: 500; letter-spacing: 0.22em; white-space: nowrap; }
  .volume { position: absolute; font-weight: 600; }
  .product-sub { position: absolute; writing-mode: vertical-rl; transform: rotate(180deg); letter-spacing: 0.3em; font-weight: 400; }

  /* tall box */
  .box-tall { left: 122px; top: 104px; width: 340px; height: 752px; }
  .box-tall .box-side { width: 120px; }
  .box-tall .box-front { width: 220px; }
  .box-tall .brand-band { top: 42px; height: 46px; font-size: 17px; }
  .box-tall .brand-dot { width: 18px; height: 18px; }
  .box-tall .product-line { left: 26px; top: 130px; font-size: 60px; }
  .box-tall .collection { left: 24px; top: 575px; font-size: 38px; }
  .box-tall .product-name { left: 30px; top: 660px; font-size: 11px; }
  .box-tall .volume { left: 98px; top: 696px; font-size: 11px; }

  /* short box */
  .box-short { left: 520px; top: 405px; width: 228px; height: 470px; }
  .box-short .box-side { width: 92px; }
  .box-short .box-front { width: 136px; }
  .box-short .brand-band { top: 40px; height: 28px; font-size: 11px; }
  .box-short .brand-dot { width: 11px; height: 11px; }
  .box-short .product-line { left: 15px; top: 92px; font-size: 36px; }
  .box-short .collection { left: 18px; top: 348px; font-size: 23px; }
  .box-short .product-name { left: 24px; top: 400px; font-size: 7px; }
  .box-short .volume { left: 58px; top: 423px; font-size: 7px; }

  /* lipstick box */
  .box-lip { left: 836px; top: 565px; width: 128px; height: 340px; }
  .box-lip .box-side { width: 40px; }
  .box-lip .box-front { width: 88px; }
  .box-lip .brand-band { top: 28px; height: 22px; font-size: 8px; gap: 4px; }
  .box-lip .brand-dot { width: 8px; height: 8px; }
  .box-lip .product-line { left: 8px; top: 76px; font-size: 27px; }
  .box-lip .product-sub { left: 43px; top: 160px; font-size: 9px; color: var(--gold); }
  .box-lip .volume { left: 40px; top: 315px; font-size: 6px; color: #fff; font-weight: 400; }
</style>
</head>
<body>
  <div class="box box-tall">
    <div class="box-side" role="img" aria-label="Repeating coral, teal and white geometric floral pattern"></div>
    <div class="box-front">
      <div class="brand-band"><span class="brand-dot"></span>MAVRA &amp; CO.</div>
      <div class="product-line">DERMAVELLE</div>
      <div class="collection">Baobin<br>&nbsp;Collection</div>
      <div class="product-name">[BALANCING TONER]</div>
      <div class="volume">75ml</div>
    </div>
  </div>

  <div class="box box-short">
    <div class="box-side" role="img" aria-label="Repeating coral, teal and white geometric floral pattern"></div>
    <div class="box-front">
      <div class="brand-band"><span class="brand-dot"></span>MAVRA &amp; CO.</div>
      <div class="product-line">DERMAVELLE</div>
      <div class="collection">Baobin<br>&nbsp;Collection</div>
      <div class="product-name">[CLEANSING OIL]</div>
      <div class="volume">25ml</div>
    </div>
  </div>

  <div class="box box-lip">
    <div class="box-side dark" role="img" aria-label="Repeating coral, teal and black geometric floral pattern"></div>
    <div class="box-front dark">
      <div class="brand-band"><span class="brand-dot"></span>MAVRA &amp; CO.</div>
      <div class="product-line">KESACOLOR</div>
      <div class="product-sub">[LIPSTICK]</div>
      <div class="volume">5ml</div>
    </div>
  </div>
</body>
</html>
```